Lurin Dasko Website

Website for my son who is in 7th grade in the US. This will prepare him to show people his accomplishments when applying for a job or going to college. It should have:
* A picture (or multiple pictures)
* A resume page
* A place to share your accomplishments
* Links to his other social profiles
* A contact form

Great to include:
* Internships (show some photos of it along with what you’ve learned).
* Volunteer work.
* A side hustle that you want to highlight

Website sample I like:
https://brisatoleno.folivane.net/brisatolenomurga

Target Market(s)

For jobs and colleges admissions.

Number of Pages Required

5+ page

Colors

Designer to choose colors to be used in the design.

Requirements
Must have
• * A picture (or multiple pictures)
• * A resume page
• * A place to share your accomplishments
• * Links to his other social profiles
• * A contact form
Nice to have
• Great to include:
• * Internships (show some photos of it along with what you’ve learned).
• * Volunteer work.
• * A side hustle that you want to highlight

```html
<!DOCTYPE html>
<html lang="en">
<head>
<meta charset="utf-8">
<title>Lurin Dasko</title>
<link rel="stylesheet" href="https://fonts.googleapis.com/css2?family=Playfair+Display:wght@900&family=Mulish:wght@400;600&family=Open+Sans:wght@400;600&display=swap">
<style>
:root{
  --teal:#1a9a8a;
  --teal-dark:#137d70;
  --ink:#555;
  --muted:#777;
  --band:#ebebeb;
  --card:#ffffff;
  --card-alt:#f7f7f7;
  --line:#cfcfcf;
  --footer:#333333;
  --white:#fff;
}
*{box-sizing:border-box;margin:0;padding:0}
html,body{width:1200px;height:3386px;overflow:hidden;background:var(--white);font-family:"Open Sans",Arial,sans-serif;color:var(--ink)}
.page{position:relative;width:1200px;height:3386px}

.site-header{position:absolute;top:0;left:0;width:1200px;height:83px;background:var(--white)}
.brand{position:absolute;left:143px;top:14px;font-family:"Playfair Display",Georgia,serif;font-weight:900;font-size:47px;color:#222;letter-spacing:-.5px;line-height:1.1}
.main-nav{position:absolute;right:145px;top:33px;display:flex;gap:32px;font-size:12.5px}
.main-nav a{color:var(--muted);text-decoration:none}
.main-nav a.active{color:var(--teal);text-decoration:underline}

.hero{position:absolute;top:83px;left:0;width:1200px;height:531px;
  background:linear-gradient(100deg,#d9c2a6 0%,#bba08a 22%,#8a8f99 38%,#2f5fb0 52%,#d9b7a0 70%,#d8b84a 86%,#e9dccb 100%)}
.hero-arrow{position:absolute;top:245px;width:40px;height:40px}
.hero-arrow.prev{left:44px}
.hero-arrow.next{right:47px}

.about{position:absolute;top:614px;left:0;width:1200px;height:431px}
.about h2{position:absolute;left:143px;top:73px;font-family:"Mulish",Arial,sans-serif;font-weight:400;font-size:41px;color:var(--teal)}
.about p{position:absolute;left:143px;top:128px;width:608px;font-size:15px;line-height:28.8px;color:var(--ink)}
.portrait{position:absolute;left:781px;top:75px;width:272px;height:272px;border-radius:50%;
  background:radial-gradient(circle at 50% 45%,#d8b89a 0%,#c7a57c 30%,#2a55a0 62%,#e8dcc3 100%)}

.section{position:absolute;left:0;width:1200px}
.section.band{background:var(--band)}
.section h2{position:absolute;top:72px;width:1200px;text-align:center;font-family:"Mulish",Arial,sans-serif;font-weight:400;font-size:42px;color:var(--teal)}
.cards{position:absolute;left:143px;top:142px;display:flex;gap:9px}
.card{width:299px;height:384px;background:var(--card)}
.section.white .card{background:var(--card-alt)}
.card .photo{height:192px}
.card h3{margin:24px 18px 0;font-family:"Mulish",Arial,sans-serif;font-weight:400;font-size:14.5px;line-height:19.5px;color:var(--teal)}
.card p{margin:13px 18px 0;font-size:10.5px;line-height:17.5px;color:var(--muted)}
.card .more{display:inline-block;margin:16px 18px 0;padding:0 16px;height:36px;line-height:34px;border:1px solid var(--line);font-size:11px;color:var(--muted);text-transform:uppercase}
.side-arrow{position:absolute;top:315px;width:38px;height:38px}
.side-arrow.prev{left:46px}
.side-arrow.next{right:47px}

.contact{position:absolute;top:2865px;left:0;width:1200px;height:425px}
.contact h2{position:absolute;top:72px;width:1200px;text-align:center;font-family:"Mulish",Arial,sans-serif;font-weight:400;font-size:42px;color:var(--teal)}
.field{position:absolute;border:1px solid var(--line);background:var(--white);font-size:12.5px;color:#999;padding:0 15px;line-height:38px}
.field.short{top:134px;width:218px;height:40px}
.field.message{top:188px;left:143px;width:912px;height:97px;line-height:1;padding-top:14px}
.submit{position:absolute;top:304px;left:548px;width:104px;height:39px;background:var(--teal);color:var(--white);font-family:"Mulish",Arial,sans-serif;font-size:15px;text-align:center;line-height:39px;text-transform:uppercase}

.site-footer{position:absolute;top:3290px;left:0;width:1200px;height:96px;background:var(--footer);color:#ccc}
.footer-links{position:absolute;left:145px;top:26px;font-size:10.5px}
.footer-links span.sep{margin:0 8px}
.copyright{position:absolute;left:145px;top:55px;font-size:10.5px}
.socials{position:absolute;left:886px;top:38px;display:flex;gap:24px}
.socials span{width:15px;height:15px;border-radius:50%;background:#cfcfcf;display:block}
</style>
</head>
<body>
<div class="page">

<header class="site-header">
  <div class="brand">Lurin Dasko</div>
  <nav class="main-nav">
    <a class="active" href="#about">About Me</a>
    <a href="#accomplishments">Accomplishments</a>
    <a href="#internships">Internships</a>
    <a href="#volunteer">Volunteer</a>
    <a href="#contact">Contact Me</a>
    <a href="#resume">Resume</a>
  </nav>
</header>

<section class="hero" role="img" aria-label="Photo of students working together at a classroom desk">
  <svg class="hero-arrow prev" viewBox="0 0 40 40"><circle cx="20" cy="20" r="19" fill="#1a9a8a" stroke="#fff" stroke-width="2"/><path d="M23 12 L15 20 L23 28" fill="none" stroke="#fff" stroke-width="3.5" stroke-linecap="round" stroke-linejoin="round"/></svg>
  <svg class="hero-arrow next" viewBox="0 0 40 40"><circle cx="20" cy="20" r="19" fill="#1a9a8a" stroke="#fff" stroke-width="2"/><path d="M17 12 L25 20 L17 28" fill="none" stroke="#fff" stroke-width="3.5" stroke-linecap="round" stroke-linejoin="round"/></svg>
</section>

<section class="about" id="about">
  <h2>About Me</h2>
  <p>Duis ornare erat eget magna dapibus, in accumsan quam pharetra. Nam tempus, quam in bibendum vulputate, sapien dolor viverra nisl, vitae euismod elit turpis et nulla. Aliquam erat volutpat. Pellentesque blandit lacus eget nunc faucibus, et tincidunt eros viverra. Phasellus consequat sagittis nisi suscipit feugiat. Cras eget leo sed nunc hendrerit ultricies eu at nisl. Praesent iaculis faucibus urna sit amet lacinia. Maecenas consequat justo enim, ac mattis massa imperdiet quis. Fusce eget neque elit. Sed augue orci, elementum in magna congue, tincidunt vulputate erat. Aliquam con sectetur orci molestie dictum molestie. Proin eget congue nulla, vel tempor diam.</p>
  <div class="portrait" role="img" aria-label="Portrait photo of Lurin in a blue striped shirt"></div>
</section>

<section class="section band" id="accomplishments" style="top:1045px;height:607px">
  <h2>Accomplishments</h2>
  <svg class="side-arrow prev" viewBox="0 0 38 38"><circle cx="19" cy="19" r="18" fill="#9a9a9a"/><path d="M22 11 L14 19 L22 27" fill="none" stroke="#fff" stroke-width="3" stroke-linecap="round" stroke-linejoin="round"/></svg>
  <div class="cards">
    <article class="card"><div class="photo" role="img" aria-label="Classroom with students raising hands to a teacher" style="background:linear-gradient(135deg,#cfe0e6,#8fb7c8 50%,#3c4456)"></div><h3>Etiam mattis augue vehicula odio posuere, sit amet tempus lectus luctus</h3><p>Pellentesque convallis molestie enim sit amet efficitur. Etiam id imperdiet lectus. Vivamus lacus justo, ultrices erat euismod iaculis mauris.</p><span class="more">Read more</span></article>
    <article class="card"><div class="photo" role="img" aria-label="Teacher helping students study in a library" style="background:linear-gradient(135deg,#7a5a3e,#3e5aa0 50%,#c9a06a)"></div><h3>Maecenas vel tortor accumsan quam varius imperdiet vel eget elit</h3><p>Pellentesque convallis molestie enim sit amet efficitur. Etiam id imperdiet lectus. Vivamus lacus justo, ultrices erat euismod iaculis mauris.</p><span class="more">Read more</span></article>
    <article class="card"><div class="photo" role="img" aria-label="Student working at a row of computers" style="background:linear-gradient(135deg,#d6d6d6,#8c8c8c 50%,#e8e8e8)"></div><h3>Aenean facilisis tincidunt lectus dictum nisi luctus eget</h3><p>Pellentesque convallis molestie enim sit amet efficitur. Etiam id imperdiet lectus. Vivamus lacus justo, ultrices erat euismod iaculis mauris.</p><span class="more">Read more</span></article>
  </div>
  <svg class="side-arrow next" viewBox="0 0 38 38"><circle cx="19" cy="19" r="18" fill="#9a9a9a"/><path d="M16 11 L24 19 L16 27" fill="none" stroke="#fff" stroke-width="3" stroke-linecap="round" stroke-linejoin="round"/></svg>
</section>

<section class="section white" id="internships" style="top:1652px;height:606px">
  <h2>Internships</h2>
  <svg class="side-arrow prev" viewBox="0 0 38 38"><circle cx="19" cy="19" r="18" fill="#9a9a9a"/><path d="M22 11 L14 19 L22 27" fill="none" stroke="#fff" stroke-width="3" stroke-linecap="round" stroke-linejoin="round"/></svg>
  <div class="cards">
    <article class="card"><div class="photo" role="img" aria-label="Bright open-plan office with desks" style="background:linear-gradient(180deg,#f0f0f0,#c8c8c8 55%,#4a4a4a)"></div><h3>Etiam mattis augue vehicula odio posuere, sit amet tempus lectus luctus</h3><p>Pellentesque convallis molestie enim sit amet efficitur. Etiam id imperdiet lectus. Vivamus lacus justo, ultrices erat euismod iaculis mauris.</p><span class="more">Read more</span></article>
    <article class="card"><div class="photo" role="img" aria-label="Intern shadowing a doctor during a patient visit" style="background:linear-gradient(135deg,#5a4630,#9a8a7a 50%,#d8d0c6)"></div><h3>Maecenas vel tortor accumsan quam varius imperdiet vel eget elit</h3><p>Pellentesque convallis molestie enim sit amet efficitur. Etiam id imperdiet lectus. Vivamus lacus justo, ultrices erat euismod iaculis mauris.</p><span class="more">Read more</span></article>
    <article class="card"><div class="photo" role="img" aria-label="Team gathered around a workbench with equipment" style="background:linear-gradient(135deg,#e4e4e4,#7d8590 50%,#d2d2d2)"></div><h3>Aenean facilisis tincidunt lectus dictum nisi luctus eget</h3><p>Pellentesque convallis molestie enim sit amet efficitur. Etiam id imperdiet lectus. Vivamus lacus justo, ultrices erat euismod iaculis mauris.</p><span class="more">Read more</span></article>
  </div>
  <svg class="side-arrow next" viewBox="0 0 38 38"><circle cx="19" cy="19" r="18" fill="#9a9a9a"/><path d="M16 11 L24 19 L16 27" fill="none" stroke="#fff" stroke-width="3" stroke-linecap="round" stroke-linejoin="round"/></svg>
</section>

<section class="section band" id="volunteer" style="top:2258px;height:607px">
  <h2>Volunteer</h2>
  <svg class="side-arrow prev" viewBox="0 0 38 38"><circle cx="19" cy="19" r="18" fill="#9a9a9a"/><path d="M22 11 L14 19 L22 27" fill="none" stroke="#fff" stroke-width="3" stroke-linecap="round" stroke-linejoin="round"/></svg>
  <div class="cards">
    <article class="card"><div class="photo" role="img" aria-label="Group of kids hiking on a country path" style="background:linear-gradient(180deg,#b8bfc6,#8d9468 55%,#cfc7b4)"></div><h3>Etiam mattis augue vehicula odio posuere, sit amet tempus lectus luctus</h3><p>Pellentesque convallis molestie enim sit amet efficitur. Etiam id imperdiet lectus. Vivamus lacus justo, ultrices erat euismod iaculis mauris.</p><span class="more">Read more</span></article>
    <article class="card"><div class="photo" role="img" aria-label="Children exploring nature in a forest" style="background:linear-gradient(135deg,#4e5a30,#2f62b0 55%,#8a6a40)"></div><h3>Maecenas vel tortor accumsan quam varius imperdiet vel eget elit</h3><p>Pellentesque convallis molestie enim sit amet efficitur. Etiam id imperdiet lectus. Vivamus lacus justo, ultrices erat euismod iaculis mauris.</p><span class="more">Read more</span></article>
    <article class="card"><div class="photo" role="img" aria-label="Kids outdoors on a field trip with a guide" style="background:linear-gradient(135deg,#6a5240,#a39a8e 50%,#3e3a36)"></div><h3>Aenean facilisis tincidunt lectus dictum nisi luctus eget</h3><p>Pellentesque convallis molestie enim sit amet efficitur. Etiam id imperdiet lectus. Vivamus lacus justo, ultrices erat euismod iaculis mauris.</p><span class="more">Read more</span></article>
  </div>
  <svg class="side-arrow next" viewBox="0 0 38 38"><circle cx="19" cy="19" r="18" fill="#9a9a9a"/><path d="M16 11 L24 19 L16 27" fill="none" stroke="#fff" stroke-width="3" stroke-linecap="round" stroke-linejoin="round"/></svg>
</section>

<section class="contact" id="contact">
  <h2>Contact Me</h2>
  <div class="field short" style="left:143px">Name</div>
  <div class="field short" style="left:375px">Email</div>
  <div class="field short" style="left:606px">Phone</div>
  <div class="field short" style="left:837px">Title</div>
  <div class="field message">Message</div>
  <div class="submit">Submit</div>
</section>

<footer class="site-footer">
  <div class="footer-links">About Me<span class="sep">|</span>Acomplishments<span class="sep">|</span>Intenships<span class="sep">|</span>Volunteer<span class="sep">|</span>Contact Me<span class="sep">|</span>Resume</div>
  <div class="copyright">Copyright © 2019 &nbsp;Lurin Dasko. &nbsp;All rights reserved.</div>
  <div class="socials" aria-label="Social profiles"><span></span><span></span><span></span><span></span><span></span></div>
</footer>

</div>
</body>
</html>
```